For Lease sign for Property management company in Kansas City

We need someone to take our information and design a standard for lease sign that we can put in front of each of our buildings. I would love for it to do its job of letting people know there are units available but also be unique somehow. Also the aspect ratio of the design would ideally be 4 wide by 3 tall but we open to other ideas. It will be a larger yard sign.

Target Market(s)

Potential Tenants

Industry/Entity Type

Real Estate Development

Font styles to use
Sans Serif

Requirements
Must have
• Our logo, our website (www.tollen-estates.com), our phone number (816) 247-5903.
Nice to have
• Some how say "For Lease"
Sign to be 4' wide by 3' tall
If there was a place to put the building name that would be cool but not ne
Should not have
• Nothing that I can think of

```html
<!DOCTYPE html>
<html lang="en">
<head>
<meta charset="utf-8">
<title>Tollen Estates – For Lease Yard Sign</title>
<link rel="stylesheet" href="https://fonts.googleapis.com/css2?family=Montserrat:wght@400;500;700&display=swap">
<style>
  :root {
    --backdrop: #f2f2f2;
    --sign-white: #ffffff;
    --ink-charcoal: #333333;
    --brand-red: #bd1630;
    --brand-gold: #f9ad3f;
    --rule-silver-dark: #8a8a8a;
    --rule-silver-light: #d4d4d4;
    --text-white: #ffffff;
  }

  * { margin: 0; padding: 0; box-sizing: border-box; }

  html, body {
    width: 800px;
    height: 1200px;
    overflow: hidden;
    background: var(--backdrop);
  }

  .canvas {
    position: relative;
    width: 800px;
    height: 1200px;
    background: var(--backdrop);
  }

  .lease-sign {
    position: absolute;
    left: 40px;
    top: 330px;
    width: 720px;
    height: 540px;
    background: var(--sign-white);
    box-shadow: 0 2px 6px rgba(0, 0, 0, 0.18);
    display: flex;
    flex-direction: column;
  }

  .sign-main {
    height: 382px;
    display: flex;
    flex-direction: column;
    align-items: center;
  }

  .sign-headline {
    margin-top: 68px;
    font-family: "Montserrat", sans-serif;
    font-weight: 700;
    font-size: 106px;
    line-height: 1;
    letter-spacing: 2px;
    color: var(--ink-charcoal);
    white-space: nowrap;
  }

  .brand-lockup {
    margin-top: 52px;
    display: flex;
    align-items: center;
    gap: 16px;
  }

  .brand-dot {
    width: 86px;
    height: 86px;
    border-radius: 50%;
    background: var(--brand-gold);
    flex-shrink: 0;
  }

  .brand-name {
    font-family: "Montserrat", sans-serif;
    font-weight: 700;
    font-size: 34px;
    line-height: 1.05;
    letter-spacing: 1px;
    color: var(--brand-red);
  }

  .silver-rule {
    height: 10px;
    background: linear-gradient(90deg,
      var(--rule-silver-dark) 0%,
      var(--rule-silver-light) 30%,
      var(--rule-silver-dark) 55%,
      var(--rule-silver-light) 85%,
      var(--rule-silver-dark) 100%);
  }

  .contact-band {
    flex: 1;
    background: var(--brand-red);
    display: flex;
    flex-direction: column;
    align-items: center;
    justify-content: center;
    color: var(--text-white);
    font-family: "Montserrat", sans-serif;
  }

  .contact-phone {
    font-weight: 500;
    font-size: 62px;
    line-height: 1;
    letter-spacing: 2px;
  }

  .contact-web {
    margin-top: 12px;
    font-weight: 400;
    font-size: 18px;
    letter-spacing: 0.5px;
  }
</style>
</head>
<body>
  <main class="canvas">
    <section class="lease-sign" aria-label="For lease yard sign">
      <div class="sign-main">
        <h1 class="sign-headline">FOR LEASE</h1>
        <div class="brand-lockup">
          <span class="brand-dot" aria-hidden="true"></span>
          <span class="brand-name">TOLLEN<br>ESTATES</span>
        </div>
      </div>
      <div class="silver-rule" aria-hidden="true"></div>
      <div class="contact-band">
        <p class="contact-phone">(816) 247-5903</p>
        <p class="contact-web">www.tollen-estates.com</p>
      </div>
    </section>
  </main>
</body>
</html>
```